House-share and Room Rental Website (With Focus on the Bedroom Landing Page)

Looking for website design for our House-share (executive accommodation) and room rental business.

Our company name is: Lodvenra could also be written as LodVenra or lodvenra. Either is fine .. just looking for a nice clean catchy logo to go with the design.

EXAMPLES
These are examples of other websites in this field that are doing well. this is a kind of baseline.
https://kelbrin.com.au/
https://www.tuvaplex.com/
https://www.nestorvi.com/
https://www.quillsa.net/
https://www.pendlebarrow.com.au/

Our business model is to rent rooms to people looking for high-quality accommodation. We fill the gap between those looking to rent rooms and those with rooms to rent. However, our model is slightly different from those already on the market as we looking to fill a massive gap in the market delivering upmarket rooms for rent.(Executive Accommodation) also in the back end will be coupled with a self management process in the back end.

We offer executive style accommodation that stands out above the rest. With special extras like fire safety.. and management processes that create happier homes. We are looking for a web design package that can help us grow and scale our business. We need a design that is captivating

Our MAIN focus is having a room landing page that stands out from the rest... The core of our business will rely on the promotion of the rooms in a share house... so the whole design relies on the BEDROOM landing page to drive results.

Target Market(s)

We have 2 markets we are aiming at ... the first market is people offering rooms to rent who want the highest rental return. The second market is people looking to rent safe, high-quality rooms, in houses that are well managed and looked after.

Industry/Entity Type

Share Economy

Logo Text

LodVenra

Number of Pages Required

5+ page

Font styles to use
Sans Serif

Colors
3276b5

Requirements
Must have
• A messaging system whereby we can create direct communication between those offering rooms and those looking for rooms.
• A call to action that says " Schedule an Inspection"
• Landing page for promoting rooms
• A home page for showing stock.
• Profile page for those selling rooms
• Profile page for those looking for rooms.
• A scheduling calendar for booking inspections
Nice to have
• Pages where new residents can lock in a room.. pay bond and rents.. and sign contracts
• Notifications
• SMS capabilities in the backend.
Should not have
• No script or handwriting fonts.

```html
<!DOCTYPE html>
<html lang="en">
<head>
<meta charset="utf-8">
<title>Lodvenra – Luxury Bed Room</title>
<link href="https://fonts.googleapis.com/css2?family=Poppins:wght@300;400;500;600;700&display=swap" rel="stylesheet">
<style>
:root{
  --navy:#10294a;
  --navy-deep:#0c2140;
  --navy-band:#2c4a6e;
  --accent:#3276b5;
  --ink:#1d2a3a;
  --muted:#6b7683;
  --line:#e3e6ea;
  --panel:#f3f4f6;
  --white:#fff;
}
*{box-sizing:border-box;margin:0;padding:0}
html,body{width:790px;height:1200px;overflow:hidden}
body{font-family:'Poppins',sans-serif;color:var(--ink);background:var(--white);position:relative;font-size:6px}
.abs{position:absolute}
ul{list-style:none}

.hero{left:0;top:0;width:790px;height:128px;background:linear-gradient(180deg,var(--navy) 0%,#12305a 100%)}
.hero-band{left:0;top:128px;width:790px;height:8px;background:var(--navy-band)}
.topbar{left:0;top:0;width:790px;height:11px;background:#1c3a60;color:#c9d4e2;font-size:5px;display:flex;align-items:center;padding:0 155px;gap:10px}
.topbar .right{margin-left:auto;display:flex;gap:10px}
.topbar svg{width:6px;height:6px;vertical-align:-1px;margin-right:2px}
.brand{color:var(--white);font-weight:600;font-size:10px;letter-spacing:.5px}
.nav{top:43px;left:314px;color:var(--white);font-size:5.4px;font-weight:500}
.nav span{position:absolute;white-space:nowrap}
.page-title{top:80px;left:0;width:790px;text-align:center;color:var(--white);font-weight:700;font-size:15px}

.gallery-main{left:155px;top:150px;width:358px;height:203px;background:linear-gradient(135deg,#b7a58a 0%,#e9e6e1 45%,#3a2f2c 75%,#d8d4cf 100%)}
.gallery-main p{position:absolute;left:13px;bottom:14px;color:#fff;font-size:7.6px;letter-spacing:.2px;text-transform:uppercase;font-weight:400;white-space:nowrap}
.thumbs{left:155px;top:358px;width:358px;height:31px;display:flex;gap:4px}
.thumbs div{flex:1;background:linear-gradient(135deg,#caa98a,#f0eeeb 60%,#8a5b4a)}
.thumb-arrow{top:358px;width:8px;height:31px;background:rgba(16,41,74,.8);color:#fff;font-size:6px;display:flex;align-items:center;justify-content:center}

.booking{left:526px;top:150px;width:110px;height:239px;background:var(--panel)}
.booking h3{text-align:center;font-size:9.5px;font-weight:600;color:var(--navy);margin-top:10px}
.booking .from{text-align:center;font-size:4.4px;font-weight:600;margin-top:5px}
.booking .price{text-align:center;font-size:15px;font-weight:600;margin-top:1px}
.booking .price small{font-size:7.5px;color:var(--muted);font-weight:400}
.booking hr{border:0;border-top:1px solid var(--line);margin:4px 0 9px}
.field{margin:0 12px}
.field label{display:block;font-size:4.4px;font-weight:600;margin-bottom:3px}
.field .box{height:12px;background:var(--white);border:1px solid var(--line);font-size:4.4px;color:#999;padding:3px 4px;margin-bottom:14px;position:relative}
.field .box b{position:absolute;right:4px;top:2px;font-weight:400;color:#888}
.btn-book{position:absolute;left:12px;top:209px;width:86px;height:18px;background:var(--navy);color:#fff;font-size:5px;font-weight:600;display:flex;align-items:center;justify-content:center}

.tabs{left:153px;top:425px}
.tab{position:absolute;left:0;width:90px;height:19px;background:var(--navy);color:#fff;font-size:5.4px;display:flex;align-items:center;padding-left:16px}
.tab i{position:absolute;left:5px;top:6px;width:7px;height:7px;border:1px solid #9fb3cc;border-radius:2px}
.tab.active{background:var(--accent);width:112px;clip-path:polygon(0 0,92% 0,100% 50%,92% 100%,0 100%);font-size:6.4px}
.vdiv{left:268px;top:415px;width:1px;height:168px;background:var(--line)}

.features{left:272px;top:420px;width:194px;display:flex;justify-content:space-between}
.feature{width:38px;text-align:center;color:var(--muted);font-size:4.2px;font-family:Georgia,serif;white-space:nowrap}
.feature svg{width:12px;height:12px;display:block;margin:0 auto 5px}
.list-title{font-size:5px;font-weight:600}
.list{margin-top:5px}
.list li{font-size:5.2px;color:#444;line-height:10.7px;padding-left:8px;position:relative;white-space:nowrap}
.list li::before{content:"";position:absolute;left:1px;top:4.5px;width:2px;height:2px;border-radius:50%;background:#444}

.contact{left:489px;top:422px;width:151px;height:144px;border:1px solid var(--line);border-right:0}
.avatar{position:absolute;left:17px;top:11px;width:34px;height:34px;border-radius:50%;background:linear-gradient(135deg,#7a4a3a,#d9b59c)}
.contact .name{position:absolute;left:75px;top:13px;font-size:7px;color:var(--ink)}
.contact .status{position:absolute;left:83px;top:22px;font-size:4px;color:var(--muted)}
.contact .rate{position:absolute;left:63px;top:34px;width:70px;height:9px;background:#eceef0;border-radius:5px;font-size:4.8px;display:flex;align-items:center;justify-content:center}
.msg{position:absolute;left:7px;top:52px;width:137px;height:44px;background:#e9ede6;border:1px solid #cfd5cb;font-size:4.6px;color:#8a8f96;padding:5px}
.btn-msg{position:absolute;left:7px;top:105px;width:137px;height:15px;background:var(--accent);color:#fff;font-size:6px;font-weight:500;display:flex;align-items:center;justify-content:center}
.btn-num{position:absolute;left:7px;top:124px;width:137px;height:15px;border:1px solid var(--accent);color:var(--accent);font-size:6px;font-weight:500;display:flex;align-items:center;justify-content:center}

.hline{left:155px;top:590px;width:481px;height:1px;background:var(--line)}
.section-title{left:155px;top:601px;font-size:8.2px;font-weight:600;letter-spacing:.2px}
.card{top:625px;width:111px}
.card .photo{height:82px;background:linear-gradient(135deg,#c9a98c,#f1efec 55%,#3c2f2b)}
.card h4{font-size:7px;font-weight:600;margin-top:9px}
.card ul{margin-top:3px}
.card li{font-size:5px;color:#555;line-height:10.8px;padding-left:11px;position:relative;white-space:nowrap}
.card li i{position:absolute;left:1px;top:3.5px;width:4px;height:4px;background:#333;border-radius:1px}
.card .view{display:inline-flex;margin-top:6px;width:41px;height:13px;border:1.5px solid var(--ink);font-size:3.8px;font-weight:600;align-items:center;justify-content:center}

.map{left:150px;top:821px;width:486px;height:131px;background:linear-gradient(135deg,#eceeef,#e3e6e8 60%,#dfe7dc)}

.newsletter{left:0;top:988px;width:790px;height:50px;background:#0f2b50}
.mail-circle{left:154px;top:1000px;width:26px;height:26px;border:1.5px solid #fff;border-radius:50%;display:flex;align-items:center;justify-content:center}
.subscribe{left:195px;top:1000px;width:185px;height:25px;background:var(--accent);color:#dbe6f3;font-size:5.4px;display:flex;align-items:center;padding-left:11px}
.subscribe .sep{position:absolute;left:151px;top:5px;width:1px;height:15px;background:#cfe0f0}
.subscribe svg{position:absolute;left:163px;top:8px}
.social{left:548px;top:1008px;display:flex;gap:18px}
.social span{width:8px;height:8px;border-radius:50%;background:#fff}

.footer{left:0;top:1038px;width:790px;height:162px;background:var(--navy-deep)}
.footer-brand{left:186px;top:1100px}
.footer-col{top:1069px;color:#b9c5d4;font-size:5.2px}
.footer-col li{line-height:14.8px}
.footer-rule{left:153px;top:1158px;width:483px;height:1px;background:#2a3f5e}
.copyright{left:153px;top:1175px;color:#fff;font-size:4.6px}
.pay{top:1175px;left:517px;display:flex;gap:13px;color:#fff;font-size:6.4px;font-weight:600}
</style>
</head>
<body>

<div class="abs hero"></div>
<div class="abs hero-band"></div>

<div class="abs topbar">
  <span><svg viewBox="0 0 10 10"><path d="M2 7h6a2 2 0 0 0 0-4 3 3 0 0 0-5.5 1A1.5 1.5 0 0 0 2 7z" fill="none" stroke="#c9d4e2"/></svg>18 ºC</span>
  <span><svg viewBox="0 0 10 10"><path d="M5 9S2 5.5 2 3.8a3 3 0 0 1 6 0C8 5.5 5 9 5 9z" fill="none" stroke="#c9d4e2"/><circle cx="5" cy="4" r="1" fill="#c9d4e2"/></svg>48 Harlow St, Brenmouth Vale</span>
  <span><svg viewBox="0 0 10 10"><path d="M2 1.5l2 .5.5 2-1 1a5 5 0 0 0 2 2l1-1 2 .5.5 2C5 9 1 5 2 1.5z" fill="none" stroke="#c9d4e2"/></svg>1-555-210-4417</span>
  <span class="right"><span>AUD ▾</span><span>ENG ▾</span></span>
</div>

<div class="abs brand" style="left:163px;top:40px">LODVENRA</div>
<nav class="abs nav">
  <span style="left:0">HOME</span>
  <span style="left:38px">FIND A ROOM</span>
  <span style="left:97px">RENT A ROOM</span>
  <span style="left:156px">GALLERY</span>
  <span style="left:201px">GALLERY ▾</span>
  <span style="left:251px">ABOUT</span>
  <span style="left:291px">CONTACT</span>
</nav>
<h1 class="abs page-title">LUXURY BED ROOM</h1>

<div class="abs gallery-main" role="img" aria-label="Photo of a luxury bedroom with a made bed and white pillows">
  <p>Executive style accommodation that stands out above the rest</p>
</div>
<div class="abs thumbs" role="img" aria-label="Thumbnail photos of bedrooms">
  <div></div><div></div><div></div><div></div><div></div><div></div><div></div>
</div>
<div class="abs thumb-arrow" style="left:155px">‹</div>
<div class="abs thumb-arrow" style="left:505px">›</div>

<aside class="abs booking">
  <h3>LODVENRA</h3>
  <p class="from">STARTING ROOM FROM</p>
  <p class="price">$330 <small>/days</small></p>
  <hr>
  <div class="field"><label>ARRIVE</label><div class="box">17/12/2019<b>▦</b></div></div>
  <div class="field"><label>DEPATURE</label><div class="box">24/12/2019<b>▦</b></div></div>
  <div class="field"><label>NO OF ROOMMATES</label><div class="box">3<b>⌄</b></div></div>
  <div class="field"><label>NO OF DAYS</label><div class="box">3<b>⌄</b></div></div>
  <div class="btn-book">BOOK NOW</div>
</aside>

<div class="abs tabs">
  <div class="tab" style="top:0"><i></i>About Me</div>
  <div class="tab" style="top:22px"><i></i>Pricing Plans</div>
  <div class="tab active" style="top:43px"><i></i>Room Details</div>
  <div class="tab" style="top:65px"><i></i>Amenities</div>
  <div class="tab" style="top:87px"><i></i>ReviewS</div>
  <div class="tab" style="top:108px"><i></i>Address</div>
</div>
<div class="abs vdiv"></div>

<div class="abs features">
  <div class="feature"><svg viewBox="0 0 12 12"><path d="M2 6L6 2l4 4v5H2z M5 11V8h2v3" fill="none" stroke="#333"/></svg>2 DOUBLE BEDS</div>
  <div class="feature"><svg viewBox="0 0 12 12"><circle cx="6" cy="4" r="2" fill="none" stroke="#333"/><path d="M3 11V8a3 3 0 0 1 6 0v3z" fill="none" stroke="#333"/></svg>4</div>
  <div class="feature"><svg viewBox="0 0 12 12"><path d="M1 6s2-3.5 5-3.5S11 6 11 6 9 9.5 6 9.5 1 6 1 6z" fill="#333"/><circle cx="6" cy="6" r="1.6" fill="#fff"/></svg>CITY</div>
  <div class="feature"><svg viewBox="0 0 12 12"><path d="M1.5 5a6.5 6.5 0 0 1 9 0M3 7a4.2 4.2 0 0 1 6 0M4.5 8.8a2 2 0 0 1 3 0" fill="none" stroke="#333"/><circle cx="6" cy="10.3" r=".8" fill="#333"/></svg>YES</div>
  <div class="feature"><svg viewBox="0 0 12 12"><path d="M2 10L10 2M2 4v3h3" fill="none" stroke="#333" stroke-width="1.3"/></svg>NO</div>
</div>

<div class="abs" style="left:278px;top:457px">
  <p class="list-title">PREFERENCES</p>
  <ul class="list"><li>Females only</li><li>Non-smoking</li><li>Minimum contract - 3 Mon</li></ul>
</div>
<div class="abs" style="left:402px;top:457px">
  <p class="list-title">TRANSPORT OPTIONS</p>
  <ul class="list"><li>Bus</li><li>Train</li><li>Distance to the city : 2km</li></ul>
</div>
<div class="abs" style="left:278px;top:511px">
  <p class="list-title">AMENITIES</p>
  <ul class="list"><li>Furnished</li><li>25 inch or larger TV</li><li>Storage space</li><li>Wardrobe</li><li>Ensuite shower</li><li>Kitchenette</li></ul>
</div>
<div class="abs" style="left:402px;top:511px">
  <p class="list-title">KEY INFORMATION</p>
  <ul class="list"><li>Size: 70 Ft²</li><li>80 $ / PER NIGHT</li><li>Friendly housemates</li><li>Private Room</li><li>Parking - street</li></ul>
</div>

<div class="abs contact">
  <div class="avatar" role="img" aria-label="Profile photo of the host"></div>
  <p class="name">Contact Maren</p>
  <p class="status">Online Today</p>
  <p class="rate">Response rate: 100% ●</p>
  <div class="msg">Login or signup to message...</div>
  <div class="btn-msg">Login to message Maren</div>
  <div class="btn-num">Login to show Maren's number</div>
</div>

<div class="abs hline"></div>
<h2 class="abs section-title">ANOTHER ACCOMMODATIONS</h2>

<article class="abs card" style="left:155px">
  <div class="photo" role="img" aria-label="Photo of a luxury room"></div>
  <h4>LUXURY ROOM</h4>
  <ul><li><i></i>Max: 2 Person(s)</li><li><i></i>Bed: King-size or twin beds</li><li><i></i>View: Ocean</li></ul>
  <span class="view">VIEW DETAIL</span>
</article>
<article class="abs card" style="left:278px">
  <div class="photo" role="img" aria-label="Photo of a family room" style="background:linear-gradient(135deg,#4a3a30,#e8e6e2 55%,#8a9a8a)"></div>
  <h4>FAMILY ROOM</h4>
  <ul><li><i></i>Max: 2 Person(s)</li><li><i></i>Bed: King-size or twin beds</li><li><i></i>View: Ocean</li></ul>
  <span class="view">VIEW DETAIL</span>
</article>
<article class="abs card" style="left:402px">
  <div class="photo" role="img" aria-label="Photo of a standard room" style="background:linear-gradient(135deg,#6a5040,#f3f2f0 50%,#c8c2bc)"></div>
  <h4>STANDARD ROOM</h4>
  <ul><li><i></i>Max: 2 Person(s)</li><li><i></i>Bed: King-size or twin beds</li><li><i></i>View: Ocean</li></ul>
  <span class="view">VIEW DETAIL</span>
</article>
<article class="abs card" style="left:525px">
  <div class="photo" role="img" aria-label="Photo of a couple room" style="background:linear-gradient(135deg,#c8b898,#ece8e0 50%,#6a4a38)"></div>
  <h4>COUPLE ROOM</h4>
  <ul><li><i></i>Max: 2 Person(s)</li><li><i></i>Bed: King-size or twin beds</li><li><i></i>View: Ocean</li></ul>
  <span class="view">VIEW DETAIL</span>
</article>

<div class="abs map" role="img" aria-label="Map showing where the room is located"></div>

<div class="abs newsletter"></div>
<div class="abs mail-circle"><svg width="13" height="10" viewBox="0 0 13 10"><rect x=".7" y=".7" width="11.6" height="8.6" fill="none" stroke="#fff"/><path d="M.7.7l5.8 5 5.8-5" fill="none" stroke="#fff"/></svg></div>
<div class="abs subscribe">Your email address<span class="sep"></span><svg width="10" height="9" viewBox="0 0 10 9"><path d="M0 0l10 4.5L0 9l1.5-4.5z" fill="#dbe6f3"/></svg></div>
<div class="abs social"><span></span><span></span><span></span><span></span></div>

<footer class="abs footer"></footer>
<div class="abs brand footer-brand">LODVENRA</div>
<ul class="abs footer-col" style="left:318px"><li>Site Map</li><li>Term &amp; Conditions</li><li>Privacy Policy</li><li>Help</li></ul>
<ul class="abs footer-col" style="left:442px"><li>Our Location</li><li>Career</li><li>About Us</li><li>Contact Us</li></ul>
<ul class="abs footer-col" style="left:565px"><li>FAQS</li><li>Rent</li><li>Search</li><li>Reviews</li></ul>
<div class="abs footer-rule"></div>
<p class="abs copyright">Copyright © 2019</p>
<div class="abs pay"><span>Paywell</span><span>VERA</span><span>Cardmo</span><span>Dinero</span></div>

</body>
</html>
```